I would like a standard letter head document that is innovative and not 'typically' corporate.
I would like a BLACK panel of some sort so that the logo can be best showcased within that (as the logo has a black background).
I would like the three words 'dream', 'believe', 'achieve'
inscribed at the side (as per the example I uploaded). Its should be more like a watermark so only just visible.
I would like the K symbol as a water mark on the page (similar to the lion on the example I uploaded).
I would like the following details also included.
Megan Tollisford
Personal Training/Nutrition/Life Coaching
www.larkvelbrook.com.au
0491 570 156
Life Coaching

```html
<!DOCTYPE html>
<html lang="en">
<head>
<meta charset="utf-8">
<title>Larkvelbrook Personal Training – Letterhead</title>
<link rel="stylesheet" href="https://fonts.googleapis.com/css2?family=Roboto:wght@400;700&display=swap">
<style>
  :root {
    --backdrop: #e7eceb;
    --paper: #ffffff;
    --teal: #1a9b98;
    --teal-dark: #0e7f7c;
    --band-black: #05040a;
    --glow-violet: #5a2bb8;
    --glow-blue: #2b4fd9;
    --ink-grey: #4a4a4a;
  }
  * { box-sizing: border-box; margin: 0; padding: 0; }
  html, body {
    width: 1200px;
    height: 849px;
    overflow: hidden;
  }
  body {
    background: var(--backdrop);
    font-family: "Roboto", Arial, sans-serif;
    display: flex;
    align-items: center;
    justify-content: center;
  }
  .letterhead {
    position: relative;
    width: 570px;
    height: 806px;
    background: var(--paper);
    box-shadow: 0 4px 18px rgba(0, 0, 0, 0.18);
  }
  .motto {
    position: absolute;
    top: 26px;
    right: 24px;
    font-size: 15px;
    letter-spacing: 0.3px;
    color: var(--band-black);
  }
  .motto .dream { color: var(--teal); }
  .motto .divider {
    color: #9a9a9a;
    margin: 0 5px;
  }
  .brand-band {
    position: absolute;
    top: 50px;
    left: 0;
    width: 100%;
    height: 86px;
    background: var(--band-black);
    border-bottom: 2px solid var(--teal);
    overflow: hidden;
  }
  .band-lights {
    position: absolute;
    inset: 0;
    background:
      radial-gradient(ellipse 140px 70px at 82% 40%, rgba(90, 43, 184, 0.75), transparent 70%),
      radial-gradient(ellipse 90px 50px at 94% 70%, rgba(43, 79, 217, 0.7), transparent 70%),
      radial-gradient(ellipse 80px 60px at 8% 60%, rgba(90, 43, 184, 0.55), transparent 70%),
      linear-gradient(90deg, var(--band-black) 40%, #140a2c 100%);
  }
  .brand-name {
    position: absolute;
    top: 18px;
    left: 30px;
    display: flex;
    align-items: center;
    gap: 12px;
  }
  .brand-dot {
    width: 40px;
    height: 40px;
    border-radius: 50%;
    border: 2px solid var(--teal);
  }
  .brand-words {
    color: var(--teal);
    font-weight: 700;
    line-height: 1;
  }
  .brand-words .title {
    display: block;
    font-size: 30px;
    letter-spacing: 0.5px;
  }
  .brand-words .sub {
    display: block;
    font-size: 13px;
    letter-spacing: 3.2px;
    margin-top: 5px;
    text-transform: uppercase;
  }
  .contact-block {
    position: absolute;
    right: 24px;
    bottom: 44px;
    padding-right: 10px;
    border-right: 2px solid var(--teal);
    text-align: right;
    color: var(--teal-dark);
    font-size: 12.5px;
    line-height: 1.25;
  }
  .contact-block .person {
    font-weight: 700;
    font-size: 14px;
  }
</style>
</head>
<body>
  <main class="letterhead">
    <p class="motto">
      <span class="dream">dream</span><span class="divider">|</span><span>believe</span><span class="divider">|</span><span>achieve</span>
    </p>

    <header class="brand-band">
      <div class="band-lights" role="img" aria-label="Glowing violet and blue light streaks on black"></div>
      <div class="brand-name">
        <span class="brand-dot"></span>
        <span class="brand-words">
          <span class="title">Larkvelbrook</span>
          <span class="sub">Personal Training</span>
        </span>
      </div>
    </header>

    <address class="contact-block">
      <p class="person">Megan Tollisford</p>
      <p>Personal Training/Nutrition/Life Coaching</p>
      <p>www.larkvelbrook.com.au</p>
      <p>0491 570 156</p>
    </address>
  </main>
</body>
</html>
```